Lumen Business Cards

We need a new look business cvard to refelect our new look website www.lumenplan.com.au
We’re Lumen, a team of town planning and traffic and transport engineering specialists located in Melbourne.

Lumen is a company that is structured, articulate, dynamic, progressive, accurate and adaptable.
Our key messages are:
1. We make your life easier by doing what we do best
2. We tell you what you need to know not what you want to hear
3. Polished and professional but not afraid to show some personality

we would like a bold new look that is polished and professional but not afraid to show a bit of personality

Target Market(s)

Lumen’s diverse client base consists of architecture practices, builders, developers, local government and the legal fraternity.

Industry/Entity Type

Town

Requirements
Must have
• must use our logo and have the following information

Joel Petrakis
Director

Lumen Advisory Pty Ltd
Hillgate first floor
Cotter Street
Kewdale VIC 3187 Australia
+61 03 9581 6724
mail@lumenplan.com.au
www.lumenplan.com.au
Nice to have
• We would like to see the logo used or the colours of the logo used.

```html
<!DOCTYPE html>
<html lang="en">
<head>
<meta charset="utf-8">
<title>Lumen Business Cards</title>
<link rel="stylesheet" href="https://fonts.googleapis.com/css2?family=Open+Sans:wght@400;600;700&display=swap">
<style>
  :root {
    --backdrop: #d9d9d6;
    --slate: #4a5661;
    --slate-deep: #3f4a54;
    --card-white: #ffffff;
    --ink: #2b2f33;
    --text-grey: #55595d;
    --accent-orange: #f39a1e;
    --wordmark-grey: #5c6670;
    --wordmark-light: #e9ecee;
  }
  * { box-sizing: border-box; margin: 0; padding: 0; }
  html, body {
    width: 1200px;
    height: 871px;
    overflow: hidden;
  }
  body {
    position: relative;
    background: var(--backdrop);
    font-family: "Open Sans", Arial, sans-serif;
  }
  .card {
    position: absolute;
    width: 580px;
    height: 331px;
    border-radius: 3px;
    box-shadow: 0 10px 28px rgba(0, 0, 0, 0.22);
  }

  /* Reverse side */
  .card--back {
    left: 80px;
    top: 100px;
    background: linear-gradient(160deg, var(--slate) 0%, var(--slate-deep) 100%);
  }
  .card--back .wordmark {
    position: absolute;
    left: 58px;
    bottom: 52px;
    font-size: 54px;
    font-weight: 400;
    letter-spacing: 1px;
    color: var(--wordmark-light);
  }

  /* Front side */
  .card--front {
    left: 540px;
    top: 450px;
    background: var(--card-white);
  }
  .brand {
    position: absolute;
    left: 52px;
    top: 132px;
    display: flex;
    align-items: center;
    gap: 12px;
  }
  .brand__square {
    width: 26px;
    height: 26px;
    background: var(--wordmark-grey);
  }
  .brand .wordmark {
    font-size: 44px;
    font-weight: 400;
    letter-spacing: 1px;
    color: var(--wordmark-grey);
    line-height: 1;
  }
  .details {
    position: absolute;
    right: 34px;
    top: 62px;
    text-align: right;
    color: var(--text-grey);
    font-size: 13px;
    line-height: 1.35;
  }
  .details__name {
    font-size: 17px;
    font-weight: 700;
    color: var(--ink);
  }
  .details__role {
    font-size: 12px;
    margin-bottom: 14px;
  }
  .details__company {
    font-weight: 700;
    color: var(--accent-orange);
    font-size: 13px;
  }
  .details__address { margin-bottom: 14px; }
  .contact-line {
    display: flex;
    justify-content: flex-end;
    align-items: center;
    gap: 14px;
  }
  .contact-line svg {
    width: 12px;
    height: 12px;
    flex: none;
  }
</style>
</head>
<body>

  <div class="card card--back">
    <span class="wordmark">Lumen</span>
  </div>

  <div class="card card--front">
    <div class="brand">
      <span class="brand__square"></span>
      <span class="wordmark">Lumen</span>
    </div>

    <div class="details">
      <div class="details__name">Joel Petrakis</div>
      <div class="details__role">Director</div>
      <div class="details__company">Lumen Advisory Pty Ltd</div>
      <div class="details__address">
        Hillgate first floor<br>
        Cotter Street<br>
        Kewdale VIC 3187 Australia
      </div>
      <div class="contact-line">
        <span>+61 03 9581 6724</span>
        <svg viewBox="0 0 12 12" aria-hidden="true">
          <path d="M2 1h2.2l1 2.6-1.3.9a6.5 6.5 0 0 0 3.6 3.6l.9-1.3 2.6 1V10a1 1 0 0 1-1 1A9 9 0 0 1 1 2a1 1 0 0 1 1-1z" fill="var(--accent-orange)"/>
        </svg>
      </div>
      <div class="contact-line">
        <span>mail@lumenplan.com.au</span>
        <svg viewBox="0 0 12 12" aria-hidden="true">
          <rect x="0.75" y="2.25" width="10.5" height="7.5" fill="none" stroke="var(--accent-orange)" stroke-width="1.2"/>
          <path d="M1 2.6 6 6.5l5-3.9" fill="none" stroke="var(--accent-orange)" stroke-width="1.2"/>
        </svg>
      </div>
      <div class="contact-line">
        <span>www.lumenplan.com.au</span>
        <svg viewBox="0 0 12 12" aria-hidden="true">
          <circle cx="6" cy="6" r="5" fill="none" stroke="var(--accent-orange)" stroke-width="1.2"/>
          <path d="M1 6h10M6 1c-2.2 2.8-2.2 7.2 0 10M6 1c2.2 2.8 2.2 7.2 0 10" fill="none" stroke="var(--accent-orange)" stroke-width="1"/>
        </svg>
      </div>
    </div>
  </div>

</body>
</html>
```